Real Estate Company / Capital Needs Cards!

need business cards designed using the logos that were just designed by sketchhive.

Reason: per designers request deadline extended 1 day…thank you.

Target Market(s)

Investors and clients looking to purchase real estate or invest in the business.

Industry/Entity Type

Business

Requirements
Must have
• two designs - one for the real estate logo and one for the capital logo, similar but slightly different.
Nice to have
• something to make it pop (perhaps on the back)
Should not have
• much color

```html
<!DOCTYPE html>
<html lang="en">
<head>
<meta charset="utf-8">
<title>Veltra Business Cards</title>
<link rel="stylesheet" href="https://fonts.googleapis.com/css2?family=Ubuntu:wght@400;500;700&display=swap">
<style>
  :root {
    --stage: #d9dadb;
    --paper: #ffffff;
    --ink: #111214;
    --charcoal: #1f2022;
    --charcoal-deep: #151618;
    --mark-grey: #6d6e70;
    --mark-light: #d6d7d8;
    --text-light: #f2f2f2;
  }
  * { box-sizing: border-box; margin: 0; padding: 0; }
  html, body { width: 1200px; height: 800px; overflow: hidden; }
  body {
    background: var(--stage);
    font-family: "Ubuntu", sans-serif;
    position: relative;
  }
  .card {
    position: absolute;
    top: 250px;
    width: 525px;
    height: 300px;
    overflow: hidden;
    box-shadow: 0 10px 24px rgba(0,0,0,0.25);
    display: flex;
    flex-direction: column;
  }
  .card--capital { left: 50px; background: var(--paper); }
  .card--estate  { left: 625px; background: var(--paper); }

  .panel-dark {
    background: radial-gradient(ellipse at 50% 30%, var(--charcoal), var(--charcoal-deep));
    color: var(--text-light);
  }
  .panel-light { background: var(--paper); color: var(--ink); }

  /* brand lockup */
  .brand { display: flex; align-items: center; gap: 12px; }
  .brand__square { width: 44px; height: 44px; border-radius: 5px; flex: none; }
  .brand__text { display: flex; flex-direction: column; }
  .brand__name { font-weight: 400; font-size: 40px; letter-spacing: 2px; line-height: 1; }
  .brand__sub { font-weight: 400; font-size: 13px; letter-spacing: 4px; text-transform: uppercase; margin-top: 4px; text-align: center; }

  /* capital card */
  .card--capital .panel-light {
    height: 172px;
    display: flex; align-items: center; justify-content: center;
    padding-left: 110px;
  }
  .card--capital .brand { flex-direction: column; gap: 8px; }
  .card--capital .brand__square { background: var(--mark-grey); width: 50px; height: 50px; }
  .card--capital .brand__name,
  .card--capital .brand__sub { color: var(--mark-grey); }
  .card--capital .panel-dark {
    flex: 1;
    padding: 22px 28px 0 0;
    text-align: right;
    font-size: 15px;
    line-height: 1.35;
  }
  .tagline { margin-bottom: 12px; }
  .web { font-size: 16px; }

  /* estate card */
  .card--estate .panel-dark {
    height: 160px;
    display: flex; align-items: center; justify-content: center;
  }
  .card--estate .brand__square { background: var(--mark-light); }
  .card--estate .brand__name,
  .card--estate .brand__sub { color: var(--mark-light); }
  .card--estate .panel-light {
    flex: 1;
    display: flex; justify-content: space-between;
    padding: 24px 26px 18px 28px;
  }
  .person__name { font-size: 20px; font-weight: 400; letter-spacing: 0.5px; }
  .person__name strong { font-weight: 700; }
  .person__title { font-size: 11px; font-weight: 700; letter-spacing: 0.5px; margin-top: 2px; }
  .contact { align-self: flex-end; font-size: 14px; line-height: 1.3; }
  .contact dt { display: inline; font-weight: 700; }
  .contact dd { display: inline; }
  .contact dd::after { content: ""; display: block; }
  .contact .gap { margin-top: 10px; }
</style>
</head>
<body>

<article class="card card--capital" aria-label="Capital business card">
  <div class="panel-light">
    <div class="brand">
      <span class="brand__square" aria-hidden="true"></span>
      <div class="brand__text">
        <span class="brand__name">VELTRA</span>
        <span class="brand__sub">Capital, LLC</span>
      </div>
    </div>
  </div>
  <div class="panel-dark">
    <p class="tagline">Lorem ipsum dolor sit amet, consectetur adipiscing elit.<br>Sed sollicitudin metus at gravida posuere.</p>
    <p class="web">www.veltrahomes.com</p>
  </div>
</article>

<article class="card card--estate" aria-label="Real estate business card">
  <div class="panel-dark">
    <div class="brand">
      <span class="brand__square" aria-hidden="true"></span>
      <div class="brand__text">
        <span class="brand__name">VELTRA</span>
        <span class="brand__sub">Real Estate</span>
      </div>
    </div>
  </div>
  <div class="panel-light">
    <div class="person">
      <p class="person__name">YOUR <strong>NAME</strong></p>
      <p class="person__title">JOB TITLE</p>
    </div>
    <dl class="contact">
      <dt>fax:</dt> <dd>555 0142 0178</dd>
      <dt>phone:</dt> <dd>555 0142 0178</dd>
      <dt class="gap">email:</dt> <dd>hello@veltrahomes.com</dd>
      <dt>website:</dt> <dd>www.veltrahomes.com</dd>
    </dl>
  </div>
</article>

</body>
</html>
```